Ridgeline Build Network Inc. Letterhead

Creation of attractive and eye catching letterhead for a business start-up for the construction industry. Letterhead must relate to construction, but avoid standard hammer and tools in the design.
Updates

I forgot to add some details, sorry about that. Some pertinent info: Ph: 916-555-0148 ridgelinebuildnet.example 487 Willowmere Ave, Ste 210 Folsom, CA 95699 info@ridgelinebuildnet.example not sure if slogan should be in there" “Connecting construction professionals to create a purpose driven industry.” must be able to be used in word. Thanks!

```html
<!DOCTYPE html>
<html lang="en">
<head>
<meta charset="utf-8">
<title>Ridgeline Build Network Inc. Letterhead</title>
<link href="https://fonts.googleapis.com/css2?family=Montserrat:wght@500;600;700&display=swap" rel="stylesheet">
<style>
  :root {
    --navy: #1c2451;
    --navy-deep: #131837;
    --red: #c0171d;
    --red-dark: #9c1217;
    --paper: #ffffff;
    --backdrop: #e9edf2;
    --faint: #eceef3;
    --ink: #1c2451;
  }
  * { margin: 0; padding: 0; box-sizing: border-box; }
  html, body {
    width: 1200px; height: 1200px; overflow: hidden;
    background: var(--backdrop);
    font-family: "Montserrat", sans-serif;
  }
  .letterhead {
    position: absolute;
    left: 211px; top: 50px;
    width: 778px; height: 1100px;
    background: var(--paper);
    box-shadow: 0 6px 24px rgba(19, 24, 55, 0.12);
  }
  .header-band {
    position: absolute; left: 0; top: 0;
    width: 100%; height: 52px;
    display: block;
  }
  .brand {
    position: absolute; top: 128px; left: 0; width: 100%;
    text-align: center; color: var(--ink);
  }
  .brand-name {
    display: inline-flex; align-items: center; gap: 10px;
    font-weight: 700; font-size: 19px; letter-spacing: 2.5px;
    text-transform: uppercase; color: var(--navy);
  }
  .brand-mark {
    width: 12px; height: 12px; background: var(--red);
  }
  .brand-tagline {
    margin-top: 10px;
    font-weight: 600; font-size: 8.5px; letter-spacing: 1.2px;
    text-transform: uppercase; color: var(--navy);
  }
  .watermark {
    position: absolute; top: 615px; left: 0; width: 100%;
    text-align: center;
    font-weight: 600; font-size: 38px; letter-spacing: 5px;
    text-transform: uppercase; color: var(--faint);
  }
  .contact {
    position: absolute; bottom: 52px; left: 0; width: 100%;
    font-weight: 500; font-size: 14px; color: var(--ink);
    text-align: center; line-height: 26px;
  }
  .contact-row { display: flex; justify-content: center; gap: 18px; }
  .contact-item { display: inline-flex; align-items: center; gap: 6px; }
  .contact-icon { width: 13px; height: 13px; fill: var(--red); flex: none; }
</style>
</head>
<body>
  <main class="letterhead">
    <svg class="header-band" viewBox="0 0 778 52" preserveAspectRatio="none" role="img" aria-label="Header band: red city skyline with cranes on the left, navy skyline on the right">
      <rect x="0" y="0" width="778" height="52" fill="var(--navy)"/>
      <polygon points="0,0 370,0 415,52 0,52" fill="var(--red)"/>
      <rect x="0" y="30" width="380" height="22" fill="var(--red-dark)" opacity="0.35"/>
      <rect x="410" y="30" width="368" height="22" fill="var(--navy-deep)" opacity="0.4"/>
    </svg>

    <header class="brand">
      <div class="brand-name"><span class="brand-mark"></span>Ridgeline Build Network</div>
      <div class="brand-tagline">Plan. Partner. Build Together.</div>
    </header>

    <div class="watermark" aria-hidden="true">Ridgeline Build Network</div>

    <footer class="contact">
      <div class="contact-row">
        <span class="contact-item">
          <svg class="contact-icon" viewBox="0 0 16 16"><path d="M3.5 1.5l2.5 0 1 3.5-1.7 1.2a9 9 0 0 0 4.5 4.5L11 9l3.5 1v2.5c0 1-1 2-2 2A11 11 0 0 1 1.5 3.5c0-1 1-2 2-2z"/></svg>
          916-555-0148
        </span>
        <span class="contact-item">
          <svg class="contact-icon" viewBox="0 0 16 16"><path d="M1 3h14v10H1z M2.5 4.5v.4L8 8.6l5.5-3.7v-.4z" fill-rule="evenodd"/></svg>
          info@ridgelinebuildnet.example
        </span>
      </div>
      <div class="contact-row">
        <span class="contact-item">
          <svg class="contact-icon" viewBox="0 0 16 16"><path d="M8 1a5 5 0 0 0-5 5c0 3.8 5 9 5 9s5-5.2 5-9a5 5 0 0 0-5-5zm0 7a2 2 0 1 1 0-4 2 2 0 0 1 0 4z"/></svg>
          487 Willowmere Ave, Ste 210, Folsom, CA 95699
        </span>
        <span class="contact-item">
          <svg class="contact-icon" viewBox="0 0 16 16"><path d="M8 1a7 7 0 1 0 0 14A7 7 0 0 0 8 1zm0 1.6c.8.9 1.4 2.3 1.6 4H6.4C6.6 4.9 7.2 3.5 8 2.6zM2.7 7.2h2.3c.1 1.5.5 2.9 1.1 4a5.4 5.4 0 0 1-3.4-4zm0-1.4a5.4 5.4 0 0 1 3.4-3.9c-.6 1.1-1 2.4-1.1 3.9zm5.3 7.6c-.8-.9-1.4-2.3-1.6-4.2h3.2c-.2 1.9-.8 3.3-1.6 4.2zm1.9-2.2c.6-1.1 1-2.5 1.1-4h2.3a5.4 5.4 0 0 1-3.4 4zM11 5.8c-.1-1.5-.5-2.8-1.1-3.9a5.4 5.4 0 0 1 3.4 3.9z"/></svg>
          ridgelinebuildnet.example
        </span>
      </div>
    </footer>
  </main>
</body>
</html>
```